An anniversary gift for my girlfriend

My girlfriend and I have been dating for almost 2 years. We met online and this has afforded us the really unique opportunity to have the first words we said to each other (the whole conversation, in fact) preserved. We're moving in together in a few months and she doesn't know that I saved the conversation. I've been waiting for this to turn it into something we can hang in our new place.

The only phrase I want to use is:
"Well if you dislike people's knees then I think we'll get along famously"

It's an Nobody Sleeps on Marlow Street reference for the curious.

I want the poster to use the words themselves as the art; I'm thinking typography. I'd like it to match her aesthetic, she likes to wear Lena Vireo and T. Dorn. Colors shouldn't be anything too "girly". Somewhere I'd like to include the date June 1, 2015. It shouldn't be a major piece of the poster though, just a way to denote the date.

It should fit (and be fully visible in) a 16x20 (inches) frame

Thanks in advance for the work!

Font styles to use
Serif
Decorative
Script

Requirements
Must have
• Must use only the words: "Well if you dislike people's knees then I think we'll get along famously"
• I want this to be typography, so making the phrase the center of the poster and the art itself.

```html
<!DOCTYPE html>
<html lang="en">
<head>
<meta charset="utf-8">
<title>Well if you dislike people's knees — anniversary poster</title>
<link rel="stylesheet" href="https://fonts.googleapis.com/css2?family=Bungee&family=Caveat:wght@400&display=swap">
<style>
  :root {
    --bg-center: #5a5a5a;
    --bg-edge: #474747;
    --letter-fill: #efd3d9;
    --letter-outline: #4a3f44;
    --letter-depth: #d98bd6;
    --date-ink: #ffffff;
  }
  html, body {
    margin: 0;
    padding: 0;
    width: 1200px;
    height: 960px;
    overflow: hidden;
  }
  .poster {
    position: relative;
    width: 1200px;
    height: 960px;
    background: radial-gradient(ellipse at 50% 40%, var(--bg-center) 0%, var(--bg-edge) 80%);
    overflow: hidden;
  }
  .phrase {
    position: absolute;
    top: 114px;
    left: 0;
    width: 1200px;
    margin: 0;
    text-align: center;
    font-family: "Bungee", "Arial Black", sans-serif;
    font-weight: 400;
    font-size: 74px;
    line-height: 90px;
    text-transform: uppercase;
    color: var(--letter-fill);
    -webkit-text-stroke: 1.5px var(--letter-outline);
    text-shadow:
      1px 1px 0 var(--letter-outline),
      2px 2px 0 var(--letter-depth),
      3px 3px 0 var(--letter-depth),
      4px 4px 0 var(--letter-depth),
      5px 5px 0 var(--letter-outline);
  }
  .phrase-line {
    display: block;
    white-space: nowrap;
  }
  .phrase-line--nudge { padding-left: 20px; }
  .phrase-line--nudge-more { padding-left: 34px; }
  .date-mark {
    position: absolute;
    right: 50px;
    bottom: 38px;
    margin: 0;
    font-family: "Caveat", cursive;
    font-size: 42px;
    color: var(--date-ink);
  }
</style>
</head>
<body>
  <main class="poster">
    <h1 class="phrase">
      <span class="phrase-line">Well if you</span>
      <span class="phrase-line">dislike people's</span>
      <span class="phrase-line">knees then</span>
      <span class="phrase-line">I think we'll</span>
      <span class="phrase-line phrase-line--nudge">get along</span>
      <span class="phrase-line phrase-line--nudge-more">famously</span>
    </h1>
    <p class="date-mark">June 1, 2015</p>
  </main>
</body>
</html>
```